Brackenford windows & Home Improvements

We are a family run business with over 35 years expertise. Myself and father run it
We supply and install a rated windows and all types of doors and
Veltrano composite doors .
We also specialise in renovating houses and adding extensions on to houses .
Are biggest selling point is the quality of the products we provide . we give 15 year guarantee on all windows and doors

I need flyers to distribute at shows and also to put through letterboxes
they can be a6 or a5 which ever works best . I have attached some images and our logo. Images don't have to be used

I have a show on the 29th march so need them fairly fast. Been designing them myself on this but they just don't look right

```html
<!DOCTYPE html>
<html lang="en">
<head>
<meta charset="utf-8">
<title>Brackenford Windows &amp; Home Improvements – Flyer</title>
<link rel="stylesheet" href="https://fonts.googleapis.com/css2?family=Oswald:wght@400;500;600&family=Dancing+Script:wght@700&display=swap">
<style>
  :root {
    --stage: #3a3a3c;
    --paper: #ffffff;
    --sky-light: #f4f5f7;
    --sky-mid: #d9dce1;
    --brand-blue: #1f4f9c;
    --ink: #3b3b3b;
    --ribbon-red: #d21f2b;
    --photo-warm: #c7a887;
    --photo-cool: #a9b6c4;
  }
  * { box-sizing: border-box; margin: 0; padding: 0; }
  html, body {
    width: 1200px; height: 927px; overflow: hidden;
    background: var(--stage);
  }
  .canvas {
    width: 1200px; height: 927px;
    display: flex; align-items: center; justify-content: center;
  }
  .flyer {
    position: relative;
    width: 1060px; height: 750px;
    background: var(--paper);
    overflow: hidden;
    font-family: "Oswald", sans-serif;
  }
  .flyer__sky {
    position: absolute; inset: 0;
    background:
      radial-gradient(ellipse 420px 260px at 82% 30%, var(--sky-mid), transparent 70%),
      radial-gradient(ellipse 380px 240px at 60% 80%, #e4e6ea, transparent 70%),
      linear-gradient(180deg, var(--sky-light), var(--paper) 90%);
  }
  .hero-photo {
    position: absolute; left: 140px; top: 0;
    width: 440px; height: 230px;
    background: linear-gradient(110deg, var(--photo-warm), var(--photo-cool));
  }
  .badge {
    position: absolute; left: 470px; top: 190px;
    width: 150px; height: 150px; border-radius: 50%;
    background: var(--paper);
    box-shadow: 0 3px 10px rgba(0,0,0,0.12);
    text-align: center;
  }
  .badge__years {
    display: block; margin-top: 22px;
    font-size: 44px; font-weight: 600; line-height: 1; color: var(--ink);
  }
  .badge__years small { font-size: 14px; vertical-align: top; }
  .badge__ribbon {
    display: block; margin: 6px auto 0; width: 118px;
    background: var(--ribbon-red); color: #fff;
    font-size: 13px; letter-spacing: 1px; padding: 2px 0;
  }
  .badge__note {
    display: block; margin-top: 6px;
    font-size: 10px; color: var(--ink); letter-spacing: .5px;
  }
  .brand {
    position: absolute; left: 660px; top: 250px;
    display: flex; align-items: center; gap: 14px;
  }
  .brand__mark { width: 26px; height: 26px; background: var(--brand-blue); flex: none; }
  .brand__name {
    font-size: 30px; font-weight: 500; color: var(--brand-blue);
    line-height: 1.05; text-transform: uppercase;
  }
  .services {
    position: absolute; left: 660px; top: 360px; width: 340px;
    font-size: 22px; font-weight: 500; color: var(--ink);
    text-transform: uppercase; line-height: 1.3; letter-spacing: .5px;
  }
  .expertise {
    position: absolute; left: 130px; top: 470px;
    color: var(--brand-blue); text-transform: uppercase;
  }
  .expertise__dots { display: block; letter-spacing: 8px; color: #9aa7bd; font-size: 16px; margin-left: 10px; }
  .expertise__line { display: flex; align-items: flex-end; gap: 10px; }
  .expertise__number { font-size: 110px; font-weight: 600; line-height: .9; }
  .expertise__over { font-family: "Dancing Script", cursive; text-transform: none; font-size: 40px; line-height: 1; }
  .expertise__years { font-size: 64px; font-weight: 600; line-height: .9; }
  .expertise__of { display: block; font-size: 60px; font-weight: 500; line-height: 1; margin-top: 6px; }
</style>
</head>
<body>
<main class="canvas">
  <article class="flyer">
    <div class="flyer__sky" role="img" aria-label="Soft white clouds in a pale sky"></div>

    <div class="hero-photo" role="img" aria-label="Photo of a white window with a view of a tree at sunset"></div>

    <div class="badge">
      <span class="badge__years">15<small>YEAR</small></span>
      <span class="badge__ribbon">GUARANTEE</span>
      <span class="badge__note">ON ALL WINDOWS AND DOORS</span>
    </div>

    <div class="brand">
      <span class="brand__mark"></span>
      <span class="brand__name">Brackenford windows<br>&amp; Home Improvements</span>
    </div>

    <p class="services">Supply and install A rated windows, all types of doors and Veltrano composite doors</p>

    <div class="expertise">
      <span class="expertise__dots">• • • • • •</span>
      <div class="expertise__line">
        <span class="expertise__number">35</span>
        <div>
          <span class="expertise__over">Over</span><br>
          <span class="expertise__years">Years</span>
        </div>
      </div>
      <span class="expertise__of">of Expertise</span>
    </div>
  </article>
</main>
</body>
</html>
```